Ranked amongst the Best Colleges and Programs

the size of the ad is Full Page, with bleed*
8”x 10.75" plus 0.25" bleed'
you have two choices for the tagline .. please chose what ever you think will allow you to make a better ad.
The instructions on the brief are in red
I am looking for a hight quality modern ad to place in local weekly publications that will stand out .
I would like a ad that people will look at and say i would like to see what this ad is all about.
I apprecate creative work.
the ad should not be very crowded and the text should be able to be read.
if you decide to use people in the ad .. (you don't have to ) then it should be a male dressed in white shirt in and sports jacket.. or if you would like you can use a vector and then use male or female people.
please leave one inch on the bottom for the footer

Target Market(s)

potential middle class students from 23-35 years of age

Industry/Entity Type

education

Requirements
Must have
• .the " 98% employment rate" should stand out in the ad.. but should not be the main part of the ad
Nice to have
• creative
Should not have
• Should not be a very busy or crowded ad.. i prefer pictures of men but should be .. in a business suit .. that looks professional- white shirt

```html
<!DOCTYPE html>
<html lang="en">
<head>
<meta charset="utf-8">
<title>Halden Masters of Accounting Ad</title>
<link href="https://fonts.googleapis.com/css2?family=Montserrat:wght@400;500;600;700&display=swap" rel="stylesheet">
<style>
  :root {
    --backdrop: #d2d2d2;
    --sky-top: #cdeffb;
    --sky-bottom: #a3e2f8;
    --stone: #eceeef;
    --paper: #ffffff;
    --ink: #2a2d34;
    --brand-blue: #3ab4e6;
    --band-blue: #1db1ea;
    --bar-grey: #8f918a;
    --ice: #c9f0ff;
  }
  * { margin: 0; padding: 0; box-sizing: border-box; }
  html, body { width: 1200px; height: 1200px; overflow: hidden; background: var(--backdrop); }
  body { font-family: "Montserrat", sans-serif; color: var(--ink); position: relative; }

  .ad {
    position: absolute; left: 154px; top: 0;
    width: 1245px; height: 1675px;
    transform: scale(0.7165); transform-origin: top left;
    background: var(--paper); overflow: hidden;
  }
  .ad__sky {
    position: absolute; left: 0; top: 0; width: 100%; height: 812px;
    background: linear-gradient(to bottom, var(--sky-top) 0%, #c4ecfa 55%, var(--sky-bottom) 100%);
  }
  .ad__stone {
    position: absolute; left: 0; top: 812px; width: 100%; height: 706px;
    background: var(--stone);
  }
  .ad__footer-space { position: absolute; left: 0; top: 1518px; width: 100%; height: 157px; background: var(--paper); }

  .ad__decor { position: absolute; left: 0; top: 0; width: 1245px; height: 1518px; }

  .headline { position: absolute; left: 64px; top: 92px; line-height: 1; }
  .headline__lead { display: block; font-size: 76px; font-weight: 600; letter-spacing: 1px; }
  .headline__key { display: block; font-size: 162px; font-weight: 700; color: var(--brand-blue); margin-top: 10px; letter-spacing: 2px; }
  .headline__tail { display: block; font-size: 96px; font-weight: 600; margin-top: 18px; letter-spacing: 1px; }

  .divider { position: absolute; left: 64px; top: 459px; width: 222px; height: 7px; background: var(--ink); border-radius: 4px; }

  .subline { position: absolute; left: 64px; top: 512px; width: 600px; font-size: 45px; line-height: 57px; font-weight: 400; }

  .ranked-band {
    position: absolute; left: 0; top: 770px; width: 512px; height: 80px;
    background: var(--band-blue); border-radius: 0 40px 40px 0;
    color: #fff; font-size: 42px; font-weight: 700; padding-left: 64px; line-height: 80px;
  }

  .rankings { position: absolute; left: 60px; top: 900px; list-style: none; }
  .rankings__item { position: relative; padding-left: 75px; font-size: 37px; line-height: 47px; font-weight: 500; margin-bottom: 58px; }
  .rankings__item strong { font-weight: 700; }
  .rankings__icon { position: absolute; left: 0; top: 8px; width: 46px; height: 40px; }

  .portrait { position: absolute; left: 590px; top: 270px; width: 590px; height: 845px; }

  .stat {
    position: absolute; left: 597px; top: 954px; width: 300px; height: 300px;
    border-radius: 50%; background: var(--ink); border: 12px solid var(--band-blue);
    box-shadow: 0 0 0 5px #fff;
    text-align: center; color: #fff;
  }
  .stat__value { display: block; font-size: 90px; font-weight: 600; color: var(--ice); margin-top: 42px; line-height: 1; letter-spacing: -2px; }
  .stat__arrow { display: block; width: 0; height: 0; margin: 12px auto 8px; border-left: 12px solid transparent; border-right: 12px solid transparent; border-top: 18px solid var(--ice); }
  .stat__label { display: block; font-size: 30px; font-weight: 600; line-height: 37px; }

  .outcomes {
    position: absolute; left: 62px; top: 1287px; width: 1125px; height: 185px;
    border: 3px dashed var(--band-blue); border-radius: 30px;
    padding: 28px 30px 0 44px; font-size: 33px; line-height: 42px; font-weight: 400;
  }
</style>
</head>
<body>
  <div class="ad">
    <div class="ad__sky"></div>
    <div class="ad__stone"></div>
    <div class="ad__footer-space"></div>

    <svg class="ad__decor" viewBox="0 0 1245 1518" aria-hidden="true">
      <line x1="755" y1="520" x2="1290" y2="75" stroke="#fff" stroke-width="66" stroke-linecap="round"/>
      <line x1="755" y1="520" x2="1290" y2="75" stroke="var(--bar-grey)" stroke-width="56" stroke-linecap="round"/>
      <path d="M1245 190 L1245 860 L880 1150 Q720 1190 640 1060 Q530 880 700 740 Z" fill="#fff"/>
      <path d="M1245 200 L1245 850 L875 1140 Q730 1175 650 1055 Q545 885 705 750 Z" fill="var(--ink)"/>
      <line x1="1090" y1="515" x2="1290" y2="355" stroke="#fff" stroke-width="140" stroke-linecap="round"/>
      <line x1="1090" y1="515" x2="1290" y2="355" stroke="#a9e4f8" stroke-width="128" stroke-linecap="round"/>
      <line x1="1095" y1="1045" x2="1290" y2="885" stroke="#fff" stroke-width="64" stroke-linecap="round"/>
      <line x1="1095" y1="1045" x2="1290" y2="885" stroke="var(--band-blue)" stroke-width="54" stroke-linecap="round"/>
    </svg>

    <h1 class="headline">
      <span class="headline__lead">MAKE YOUR</span>
      <span class="headline__key">RESUME</span>
      <span class="headline__tail">STAND OUT</span>
    </h1>
    <div class="divider"></div>
    <p class="subline">with a prestigious Halden-Masters of Accounting Degree.</p>

    <div class="ranked-band">Ranked amongst:</div>
    <ul class="rankings">
      <li class="rankings__item">
        <svg class="rankings__icon" viewBox="0 0 46 40"><path d="M23 2 L45 12 L23 22 L1 12 Z" fill="var(--brand-blue)"/><path d="M10 18 V28 Q23 38 36 28 V18 L23 24 Z" fill="var(--brand-blue)"/><rect x="40" y="12" width="3" height="16" fill="var(--brand-blue)"/></svg>
        Best Colleges -<br><strong>Meridian Review 2023</strong>
      </li>
      <li class="rankings__item">
        <svg class="rankings__icon" viewBox="0 0 46 40"><path d="M23 2 L45 12 L23 22 L1 12 Z" fill="var(--brand-blue)"/><path d="M10 18 V28 Q23 38 36 28 V18 L23 24 Z" fill="var(--brand-blue)"/><rect x="40" y="12" width="3" height="16" fill="var(--brand-blue)"/></svg>
        Best Masters in<br>Accounting Degree -<br><strong>Globegrade 2023</strong>
      </li>
    </ul>

    <svg class="portrait" viewBox="0 0 590 845" role="img" aria-label="Photo of a smiling bearded man in a white blazer and light blue shirt">
      <defs>
        <linearGradient id="portraitTone" x1="0" y1="0" x2="0" y2="1">
          <stop offset="0" stop-color="#c9a48c"/>
          <stop offset="0.35" stop-color="#e9e6e2"/>
          <stop offset="1" stop-color="#cfe0ee"/>
        </linearGradient>
      </defs>
      <path d="M190 60 Q270 0 350 60 L355 280 L520 360 L590 780 L545 845 L40 845 L0 700 L30 360 L190 280 Z" fill="url(#portraitTone)"/>
    </svg>

    <div class="stat">
      <span class="stat__value">98%</span>
      <span class="stat__arrow"></span>
      <span class="stat__label">employment<br>rate</span>
    </div>

    <p class="outcomes">HSP graduates have gone on to work in various high-quality jobs in top firms, earning impressive six-figure salaries as well as opening successful businesses.</p>
  </div>
</body>
</html>
```